Personal Injury Law Firm Marketing Postcards

Looking for 4 different high quality graphic postcards (print on both sides of 4"x6" postcard to market a Personal Injury Lawyer (Walter Dunmore). These will be placed on cars and in stores on stands. My photo and/or stock images.... We are targeting People who have been injured in automobile accidents, motorcycle accidents, slip and fall (wet/greasy floors indoors in supermarkets, restaurants, etc., snow and ice outdoors on sidewalks) trip and fall cases on dangerous staircases. indoor/outdoor, dog bite injuries. ( I like the use of stock images of these type of injury causing accidents. You can use following language "Serving People Injured in NY & NJ" . Millions of Dollars Recovered, Free Consultation and No Fee Unless We Recover Money! Phone number to be displayed (555) 614-3082 "call or text" Available 24 hours a day 7 days per week. May also want to mention that we can take over your case from another lawyer if you are not satisfied with your current attorney. There should be a small space in corner which has a space for my marketing person to handwrite in their reference code.

Target Market(s)

18-75 years old - densely populated major city

Industry/Entity Type

Legal

Font styles to use
Other font styles liked:
• Please use logo style that I uploaded.. Please do not just cut parts of my website out and use them. Do not use LOGO from my website

Colors
0054AA
0677BA
7BADD7
CADEEF
E8F1F8
00AB8E
00BBA5
67D7C9
C6EFE9
E9F9F6

Requirements
Must have
• Professional Appearance

```html
<!DOCTYPE html>
<html lang="en">
<head>
<meta charset="utf-8">
<title>Walter Dunmore Postcards</title>
<link rel="stylesheet" href="https://fonts.googleapis.com/css2?family=Montserrat:ital,wght@0,400;0,500;0,800;1,400&display=swap">
<style>
  :root {
    --page-bg: #ececec;
    --card-bg: #ffffff;
    --gold: #dcc07a;
    --gold-soft: #e6cf8f;
    --gold-text: #cfa957;
    --ink: #111111;
    --ink-soft: #222222;
    --line: #111111;
  }
  * { margin: 0; padding: 0; box-sizing: border-box; }
  html, body { width: 1200px; height: 1200px; overflow: hidden; }
  body { background: var(--page-bg); font-family: "Montserrat", Arial, sans-serif; color: var(--ink); }
  .stage { position: absolute; left: 0; top: 0; width: 960px; height: 960px; transform: scale(1.25); transform-origin: 0 0; }
  .postcard { position: absolute; left: 167px; width: 628px; height: 418px; background: var(--card-bg); overflow: hidden; box-shadow: 0 6px 14px rgba(0,0,0,0.12); }
  .postcard--front { top: 44px; }
  .postcard--back { top: 500px; }
  .shapes { position: absolute; inset: 0; width: 100%; height: 100%; }
  .firm-name { position: absolute; color: var(--gold-text); font-weight: 500; text-transform: uppercase; line-height: 1.05; text-align: center; white-space: nowrap; }
  .postcard--front .firm-name { left: 4px; top: 117px; width: 170px; font-size: 15px; letter-spacing: -0.6px; }
  .postcard--back .firm-name { left: 211px; top: 183px; width: 120px; font-size: 9.8px; letter-spacing: -0.4px; }
  .offer { position: absolute; line-height: 1.15; white-space: nowrap; }
  .offer__lead { font-size: 16px; font-weight: 400; }
  .offer__title { font-size: 28px; font-weight: 800; letter-spacing: -0.2px; line-height: 1.05; }
  .offer__terms { font-size: 13.5px; font-weight: 400; }
  .postcard--front .offer { right: 29px; top: 23px; text-align: right; }
  .postcard--back .offer { left: 29px; top: 24px; }
  .postcard--back .offer__title { color: var(--gold-text); }
  .case-list { position: absolute; left: 29px; list-style: none; font-style: italic; font-size: 12.5px; line-height: 15.6px; color: var(--ink-soft); white-space: nowrap; }
  .postcard--front .case-list { top: 322px; }
  .postcard--back .case-list { top: 265px; }
  .contact-phone, .contact-area { position: absolute; display: flex; align-items: center; gap: 7px; white-space: nowrap; }
  .postcard--front .contact-phone { right: 28px; top: 330px; font-size: 24px; font-weight: 500; }
  .postcard--front .contact-area { right: 28px; top: 366px; font-size: 14px; }
  .postcard--back .contact-phone { left: 28px; top: 339px; font-size: 17.5px; font-weight: 500; }
  .postcard--back .contact-area { left: 31px; top: 372px; font-size: 14px; }
  .icon { display: block; }
  .stamp-box { position: absolute; left: 524px; top: 25px; width: 71px; height: 80px; border: 2px solid var(--line); }
  .address-line { position: absolute; left: 389px; width: 206px; height: 0; border-top: 2px solid var(--line); }
</style>
</head>
<body>
<div class="stage">

  <section class="postcard postcard--front">
    <svg class="shapes" viewBox="0 0 628 418">
      <defs>
        <linearGradient id="courtBase" x1="0" y1="0" x2="0" y2="1">
          <stop offset="0" stop-color="#2a2f38"/>
          <stop offset="0.45" stop-color="#3a2f2a"/>
          <stop offset="0.8" stop-color="#5e3a22"/>
          <stop offset="1" stop-color="#3a281d"/>
        </linearGradient>
        <radialGradient id="courtGlow" cx="0.42" cy="0.68" r="0.45">
          <stop offset="0" stop-color="#a8683a" stop-opacity="0.85"/>
          <stop offset="0.5" stop-color="#7a4a2a" stop-opacity="0.45"/>
          <stop offset="1" stop-color="#3a281d" stop-opacity="0"/>
        </radialGradient>
        <radialGradient id="courtLight" cx="0.72" cy="0.35" r="0.35">
          <stop offset="0" stop-color="#8c7a68" stop-opacity="0.55"/>
          <stop offset="1" stop-color="#8c7a68" stop-opacity="0"/>
        </radialGradient>
        <linearGradient id="portraitBase" x1="0" y1="0" x2="0" y2="1">
          <stop offset="0" stop-color="#ffffff"/>
          <stop offset="0.3" stop-color="#d9dde3"/>
          <stop offset="0.5" stop-color="#4a5568"/>
          <stop offset="1" stop-color="#1f2736"/>
        </linearGradient>
        <radialGradient id="portraitShade" cx="0.5" cy="0.75" r="0.6">
          <stop offset="0" stop-color="#3b4a66" stop-opacity="0.7"/>
          <stop offset="1" stop-color="#1a2130" stop-opacity="0"/>
        </radialGradient>
      </defs>
      <g role="img" aria-label="Photo of a wooden gavel and a statue of Justice in a law library">
        <polygon points="130,0 400,0 473,321 218,321" fill="url(#courtBase)"/>
        <polygon points="130,0 400,0 473,321 218,321" fill="url(#courtLight)"/>
        <polygon points="130,0 400,0 473,321 218,321" fill="url(#courtGlow)"/>
      </g>
      <polygon points="151,186 193,186 238,291 196,291" fill="var(--gold-soft)"/>
      <polygon points="270,0 628,0 628,103 298,103" fill="var(--gold)"/>
      <g role="img" aria-label="Portrait of the attorney in a dark suit">
        <polygon points="470,106 600,106 600,258 555,300 470,300" fill="url(#portraitBase)"/>
        <polygon points="470,106 600,106 600,258 555,300 470,300" fill="url(#portraitShade)"/>
      </g>
    </svg>

    <div class="firm-name">Law Office of<br>Walter Dunmore</div>

    <div class="offer">
      <p class="offer__lead">Millions of Dollars Recovered</p>
      <p class="offer__title">Free Consultation</p>
      <p class="offer__terms">and No Fee Unless We Recover Money!</p>
    </div>

    <ul class="case-list">
      <li>Automobile accidents</li>
      <li>Motorcycle accidents</li>
      <li>Slip and fall (wet / greasy floors</li>
      <li>Indoors in supermarkets, restaurants, etc...</li>
    </ul>

    <div class="contact-phone">
      <span>(555) 614-3082</span>
      <svg class="icon" width="22" height="22" viewBox="0 0 24 24"><circle cx="12" cy="12" r="10.5" fill="none" stroke="#111" stroke-width="2"/><path d="M8.2 6.8l2 .2.8 2.6-1.3 1.2c.7 1.5 1.9 2.7 3.4 3.4l1.2-1.3 2.6.8.2 2c-.3.8-1.2 1.3-2 1.2-3.9-.6-7-3.7-7.6-7.6-.1-.8.4-1.7 1.2-2z" fill="#111"/></svg>
    </div>
    <div class="contact-area">
      <span>New Jersey and New York</span>
      <svg class="icon" width="11" height="13" viewBox="0 0 12 14"><path d="M6 1a3.4 3.4 0 0 0-3.4 3.4C2.6 7 6 10 6 10s3.4-3 3.4-5.6A3.4 3.4 0 0 0 6 1z" fill="none" stroke="#111" stroke-width="1.4"/><path d="M1.5 12.5h9" stroke="#111" stroke-width="1.4"/></svg>
    </div>
  </section>

  <section class="postcard postcard--back">
    <svg class="shapes" viewBox="0 0 628 418">
      <defs>
        <linearGradient id="gavelBase" x1="0" y1="0" x2="0" y2="1">
          <stop offset="0" stop-color="#1e2530"/>
          <stop offset="0.35" stop-color="#6b4326"/>
          <stop offset="0.6" stop-color="#8a5a32"/>
          <stop offset="1" stop-color="#2a1d16"/>
        </linearGradient>
        <radialGradient id="gavelShine" cx="0.65" cy="0.5" r="0.4">
          <stop offset="0" stop-color="#c9a24a" stop-opacity="0.6"/>
          <stop offset="1" stop-color="#c9a24a" stop-opacity="0"/>
        </radialGradient>
        <radialGradient id="gavelShade" cx="0.85" cy="0.2" r="0.5">
          <stop offset="0" stop-color="#111" stop-opacity="0.6"/>
          <stop offset="1" stop-color="#111" stop-opacity="0"/>
        </radialGradient>
      </defs>
      <g role="img" aria-label="Photo of a gavel with a gold band in front of stacked law books">
        <rect x="0" y="107" width="220" height="166" fill="url(#gavelBase)"/>
        <rect x="0" y="107" width="220" height="166" fill="url(#gavelShine)"/>
        <rect x="0" y="107" width="220" height="166" fill="url(#gavelShade)"/>
      </g>
      <polygon points="0,243 100,207 221,274 0,274" fill="var(--card-bg)"/>
    </svg>

    <div class="offer">
      <p class="offer__lead">Millions of Dollars Recovered</p>
      <p class="offer__title">Free Consultation</p>
      <p class="offer__terms">and No Fee Unless We Recover Money!</p>
    </div>

    <div class="firm-name">Law Office of<br>Walter Dunmore</div>

    <ul class="case-list">
      <li>Automobile accidents</li>
      <li>Motorcycle accidents</li>
      <li>Slip and fall (wet / greasy floors</li>
      <li>Indoors in supermarkets, restaurants, etc...</li>
    </ul>

    <div class="contact-phone">
      <svg class="icon" width="16" height="16" viewBox="0 0 24 24"><circle cx="12" cy="12" r="10.5" fill="none" stroke="#111" stroke-width="2"/><path d="M8.2 6.8l2 .2.8 2.6-1.3 1.2c.7 1.5 1.9 2.7 3.4 3.4l1.2-1.3 2.6.8.2 2c-.3.8-1.2 1.3-2 1.2-3.9-.6-7-3.7-7.6-7.6-.1-.8.4-1.7 1.2-2z" fill="#111"/></svg>
      <span>(555) 614-3082</span>
    </div>
    <div class="contact-area">
      <svg class="icon" width="11" height="13" viewBox="0 0 12 14"><path d="M6 1a3.4 3.4 0 0 0-3.4 3.4C2.6 7 6 10 6 10s3.4-3 3.4-5.6A3.4 3.4 0 0 0 6 1z" fill="none" stroke="#111" stroke-width="1.4"/><path d="M1.5 12.5h9" stroke="#111" stroke-width="1.4"/></svg>
      <span>New Jersey and New York</span>
    </div>

    <div class="stamp-box"></div>
    <div class="address-line" style="top:280px"></div>
    <div class="address-line" style="top:317px"></div>
    <div class="address-line" style="top:353px"></div>
  </section>

</div>
</body>
</html>
```